Pelton|Marsh & Quillan business card contest

We need a logo for an upscale boutique diversified company involved in real estate, investments, cattle, and more. Our businesses DO NOT need to be reflected in the business card nor do we want them noted. This is our logo and colors and we love our logo and colors. Our logo looks best against a black background and we like to include the firm name in our logo usage. importantly, the names Pelton and Marsh are separated by | not / and we use an ampersand not the word and.
On the front of the card, we want to include:
company logo and name (Pelton|Marsh & Quillan)
on the back, we would definitely include:
address, email, cell #
logo and name (smaller size than front)

The variable will be location of individual name and title (mine for example is ) - whether on the front OR on the back. interested in variations from which to choose
Dr. Neil R. Whitcombe, CFA
Scientifique des Fusées Financières

we would like to use contemporary symbols for address, email address, cell # with an option for web site that we do not intend to use initially. we like two sided cards and believe this design should use four rounded corners with the standard size. we prefer thicker card stock and may look at metal.

```html
<!DOCTYPE html>
<html lang="en">
<head>
<meta charset="utf-8">
<title>Pelton|Marsh &amp; Quillan — Business Card</title>
<link rel="stylesheet" href="https://fonts.googleapis.com/css2?family=Open+Sans:wght@400&display=swap">
<style>
  :root {
    --page: #ffffff;
    --card-dark-a: #232021;
    --card-dark-b: #343233;
    --card-light: #ffffff;
    --card-edge: #6b6b6b;
    --slate: #646464;
    --slate-dim: #5e5e5e;
    --ink: #1e1e1e;
    --ember-a: #d4672a;
    --ember-b: #f08c2a;
  }
  html, body {
    margin: 0;
    width: 1200px;
    height: 1200px;
    overflow: hidden;
    background: var(--page);
    font-family: "Open Sans", Arial, sans-serif;
  }
  .sheet { position: relative; width: 1200px; height: 1200px; }

  .card {
    position: absolute;
    top: 393px;
    width: 553px;
    height: 361px;
    box-sizing: border-box;
    overflow: hidden;
  }
  .card--front {
    left: 41px;
    background: linear-gradient(135deg, var(--card-dark-b) 0%, var(--card-dark-a) 30%, var(--card-dark-b) 55%, var(--card-dark-a) 100%);
  }
  .card--back {
    left: 613px;
    background: var(--card-light);
    border: 1px solid var(--card-edge);
  }

  .band { position: absolute; }
  .band--slate { background: var(--slate); }
  .band--ember { background: linear-gradient(90deg, var(--ember-a), var(--ember-b)); }

  .card--front .band--slate { left: 10px; top: 0; width: 114px; height: 40px; opacity: .85; }
  .card--front .band--ember { left: 478px; bottom: 0; width: 65px; height: 32px; }
  .card--back .band--slate { left: 428px; top: 0; width: 115px; height: 40px; }
  .card--back .band--ember { left: 11px; bottom: 0; width: 65px; height: 32px; }

  .wordmark {
    position: absolute;
    white-space: nowrap;
    font-weight: 400;
    color: var(--slate-dim);
    letter-spacing: .01em;
  }
  .card--front .wordmark {
    left: 0; right: 0;
    top: 162px;
    text-align: center;
    font-size: 31px;
  }
  .wordmark-square {
    display: inline-block;
    width: 14px; height: 14px;
    background: var(--ember-b);
    margin-right: 12px;
    vertical-align: 3px;
  }
  .card--back .wordmark {
    left: 420px;
    top: 86px;
    width: 120px;
    text-align: center;
    font-size: 10.5px;
    color: var(--ink);
  }

  .person { position: absolute; left: 44px; top: 106px; }
  .person-name { margin: 0; font-size: 22px; font-weight: 400; color: var(--ink); line-height: 1.1; }
  .person-title { margin: 2px 0 0; font-size: 10.5px; color: var(--ember-b); }

  .contacts { position: absolute; left: 260px; top: 183px; margin: 0; padding: 0; list-style: none; }
  .contact { position: absolute; left: 0; display: flex; align-items: center; white-space: nowrap; font-size: 12px; color: var(--ink); }
  .contact svg { width: 24px; height: 22px; fill: var(--ink); }
  .contact-text { position: absolute; left: 61px; }
  .contact--mail { top: 0; }
  .contact--cell { top: 29px; }
  .contact--phone { top: 63px; }
  .contact--place { top: 97px; }
</style>
</head>
<body>
<main class="sheet">

  <section class="card card--front" aria-label="Card front">
    <div class="band band--slate"></div>
    <p class="wordmark"><span class="wordmark-square"></span>Pelton|Marsh &amp; Quillan</p>
    <div class="band band--ember"></div>
  </section>

  <section class="card card--back" aria-label="Card back">
    <div class="band band--slate"></div>
    <p class="wordmark">Pelton|Marsh &amp; Quillan</p>

    <div class="person">
      <h1 class="person-name">Dr. Neil R. Whitcombe, CFA</h1>
      <p class="person-title">Scientifique des Fusées Financières</p>
    </div>

    <ul class="contacts">
      <li class="contact contact--mail">
        <svg viewBox="0 0 24 22" aria-hidden="true"><path d="M2 5h20v13H2z M3.5 6.5l8.5 6.5 8.5-6.5 M3.5 16.5l6.5-5.5 M20.5 16.5l-6.5-5.5" fill="none" stroke="#1e1e1e" stroke-width="1.6"/></svg>
        <span class="contact-text">neil@peltonmarsh.net</span>
      </li>
      <li class="contact contact--cell">
        <svg viewBox="0 0 24 22" aria-hidden="true"><rect x="7" y="1" width="10" height="20" rx="1.5" fill="none" stroke="#1e1e1e" stroke-width="1.6"/><rect x="10.5" y="18" width="3" height="1.2"/></svg>
        <span class="contact-text">(+971) 555 018 2244</span>
      </li>
      <li class="contact contact--phone">
        <svg viewBox="0 0 24 22" aria-hidden="true"><path d="M5 2l3.5-.5 2 4.5-2 1.8c1 2.6 3.2 5 5.8 6.2l1.9-2 4.3 2.1-.5 3.4c-.3 1.3-1.6 2-2.9 1.8C10 18.1 4.4 12.4 3.6 5.1 3.4 3.7 4 2.4 5 2z"/></svg>
        <span class="contact-text">(+971) 55 018 7731</span>
      </li>
      <li class="contact contact--place">
        <svg viewBox="0 0 24 22" aria-hidden="true"><path d="M12 1a7 7 0 0 0-7 7c0 5 7 13 7 13s7-8 7-13a7 7 0 0 0-7-7zm0 4.3a2.8 2.8 0 1 1 0 5.6 2.8 2.8 0 0 1 0-5.6z" fill-rule="evenodd"/></svg>
        <span class="contact-text">Marina Row, Dubai, UAE</span>
      </li>
    </ul>

    <div class="band band--ember"></div>
  </section>

</main>
</body>
</html>
```